Home page web design for a lawn specialist business

-The design must be based around the attached HPID (home page information design) called Turf Tidings HPID. I've attached Word and PDF versions - these are the same. The table boxes are just for approximate placement of information and you can use boxes and bold shapes for this design.

All fonts used in the HPID are only examples - you can use any Google font you wish.

- Text that is in orange is for your information only. Text to go on the design is black. Some instructions are in the HPID. Please be creative!

-The design needs to be modern and exciting - colours are to be the green of the logo, and white ...and then choose dark green, or dark grey or black.

Logo - attached (it's not great quality but don't worry, we'll replace it later)

- I've provided the images for the galleries - they are labelled and will match the name in the HPID. Please use the supplied images!

- Examples of some websites that have great design... don't copy them please but they are similar in look to what we are after....
www.qmbbuildworks.co.nz
http://www.rim-safeguard.co.nz/
http://www.lumenhomes.wb.gs/

Important: Width of content will be 1280 pixels when implemented as a web page but the winning design will need to supplied be on a 2000 pixel wide background so nav bars and background can extend outside the 1280 width.
Header height (without nav bar) 150-160 pixels.

We don't comment on individual designs but will choose a winning design promptly.

Industry/Entity Type

Business

Number of Pages Required

1 page

Font styles to use
Sans Serif

Requirements
Must have
• clean, modern, well-spaced design

```html
<!DOCTYPE html>
<html lang="en">
<head>
<meta charset="utf-8">
<title>Turf Tidings – Lawn Specialists</title>
<link href="https://fonts.googleapis.com/css2?family=Open+Sans:ital,wght@0,400;0,600;0,700;1,400&display=swap" rel="stylesheet">
<style>
:root{
  --green:#3aa63c;
  --green-dark:#2a8a2f;
  --green-deep:#1f7326;
  --nav:#2b2b2b;
  --ink:#2c2c2c;
  --muted:#555;
  --white:#fff;
  --field:#efefef;
}
*{box-sizing:border-box;margin:0;padding:0}
html,body{width:1200px;height:2439px;overflow:hidden}
body{font-family:"Open Sans",Arial,sans-serif;color:var(--ink);background:var(--white);position:relative}
.wrap{position:absolute;left:119px;width:961px}
.btn{display:inline-block;background:var(--green);color:var(--white);font-size:11px;font-weight:700;text-transform:uppercase;padding:8px 15px;letter-spacing:.2px;white-space:nowrap}

/* header */
.site-header{position:absolute;top:0;left:0;width:1200px;height:120px}
.brand{position:absolute;left:119px;top:18px;display:flex;align-items:center;gap:12px}
.brand-mark{width:74px;height:74px;background:var(--green)}
.brand-name{font-size:24px;font-weight:700;color:var(--green)}
.tagline{position:absolute;left:449px;top:36px}
.tagline h2{font-size:23px;font-weight:700;color:var(--green);letter-spacing:.5px;line-height:1.1}
.tagline p{font-size:13px;color:var(--muted);font-weight:600}
.contact{position:absolute;right:120px;top:34px;text-align:right}
.contact small{font-size:12px;color:var(--muted);letter-spacing:.3px;display:block}
.contact .phone{font-size:27px;font-weight:700;color:var(--green);display:flex;align-items:center;gap:8px;justify-content:flex-end;margin-top:2px}

/* nav */
.main-nav{position:absolute;top:120px;left:0;width:1200px;height:38px;background:var(--nav);border-bottom:3px solid #111}
.main-nav ul{list-style:none;display:flex;position:absolute;left:119px;height:35px}
.main-nav li{font-size:11px;color:var(--white);text-transform:uppercase;line-height:35px;text-align:center;border-right:1px solid #3c3c3c;white-space:nowrap}
.main-nav li.active{background:var(--green)}

/* slider */
.hero{top:176px;height:312px;background:var(--white);box-shadow:0 0 6px rgba(0,0,0,.25);padding:3px}
.hero-shadow{position:absolute;left:150px;top:486px;width:900px;height:20px;background:radial-gradient(ellipse at center,rgba(0,0,0,.45),rgba(0,0,0,0) 70%)}
.hero-photos{display:flex;height:306px}
.photo-before{width:478px;background:linear-gradient(180deg,#d9d4c6 0%,#8a6e58 45%,#6c5442 100%)}
.photo-after{flex:1;background:linear-gradient(180deg,#e3e0d5 0%,#7fb24b 35%,#4f9a2c 100%)}
.hero-label{position:absolute;background:rgba(40,40,40,.78);color:var(--white);font-size:27px;font-weight:700;padding:6px 14px;white-space:nowrap}
.hero-arrow{position:absolute;top:140px;width:30px;height:30px;background:var(--green);display:flex;align-items:center;justify-content:center}

/* grass bands */
.grass{position:absolute;left:0;width:1200px;background:linear-gradient(180deg,#ffffff 0%,#8fd16a 30%,#3f9e2c 100%)}

/* intro */
.intro{position:absolute;top:572px;left:0;width:1200px;height:222px;background:var(--green-dark);color:var(--white)}
.intro h1{text-align:center;font-size:29px;font-weight:400;margin-top:10px}
.intro h3{text-align:center;font-size:21px;font-weight:600}
.intro .rule{width:530px;margin:14px auto 0;border-top:1px dashed rgba(255,255,255,.6)}
.intro .cols{position:absolute;left:119px;top:124px;width:961px;display:flex;gap:22px}
.intro .cols p{flex:1;font-size:12px;line-height:1.5;text-align:justify}

/* services */
.services{position:absolute;top:794px;left:0;width:1200px;height:715px;background:var(--green)}
.card{position:absolute;width:470px;height:319px;background:var(--white);padding:19px 22px}
.card h4{font-size:13px;font-weight:700;margin-bottom:14px}
.card .pic{height:150px;margin-bottom:18px}
.card p{font-size:10.5px;line-height:1.45;color:#444;letter-spacing:-.1px}
.card .btn{position:absolute;left:22px;bottom:24px}

/* video */
.video-title{top:1535px;width:600px;font-size:14px;font-weight:700;line-height:1.3}
.video{position:absolute;left:119px;top:1592px;width:599px;height:246px;border:3px solid #fff;box-shadow:0 0 4px rgba(0,0,0,.3);background:linear-gradient(180deg,#b9c7b6 0%,#6e9a52 55%,#4f8b2e 100%)}
.video-shadow{position:absolute;left:150px;top:1838px;width:540px;height:22px;background:radial-gradient(ellipse at center,rgba(0,0,0,.45),rgba(0,0,0,0) 70%)}
.play{position:absolute;left:269px;top:88px;text-align:center;color:#fff;font-size:14px;font-weight:700;white-space:nowrap}
.play span{display:flex;width:60px;height:42px;background:rgba(255,255,255,.92);border-radius:6px;align-items:center;justify-content:center;margin:0 auto 4px}
.why{position:absolute;left:742px;top:1530px;width:338px}
.why h3{font-size:24px;font-weight:700;display:inline-block;padding-bottom:8px;border-bottom:3px solid var(--green)}
.why h3 em{font-style:normal;color:var(--green)}
.why ul{list-style:none;margin-top:35px;padding-left:7px}
.why li{display:flex;gap:12px;font-size:11px;line-height:1.45;color:#444;margin-bottom:15px}
.why li svg{flex:none;margin-top:2px}

/* testimonial */
.testimonial{position:absolute;top:1875px;left:0;width:1200px;height:239px;background:var(--green)}
.testimonial h5{position:absolute;left:119px;top:25px;width:420px;color:#fff;font-size:12.5px;font-weight:700;text-transform:uppercase;line-height:1.35}
.quote{position:absolute;left:119px;top:68px;width:470px;height:92px;background:#f3f3f3;padding:22px 30px 0 50px;font-size:12px;font-style:italic;color:#555;line-height:1.5}
.quote .mark{position:absolute;left:26px;top:10px;font-size:32px;color:#777;font-style:normal}
.quote-tail{position:absolute;left:512px;top:160px;width:0;height:0;border-left:16px solid transparent;border-top:14px solid #f3f3f3}
.cite{position:absolute;left:119px;top:180px;width:435px;text-align:right;color:#fff;font-size:11px;line-height:1.3}
.cite b{display:block;font-weight:700}
.testimonial .pic{position:absolute;left:611px;top:54px;width:469px;height:154px;background:linear-gradient(180deg,#9fb58e 0%,#5aa73a 45%,#3e8f23 100%)}

/* footer */
.site-footer{position:absolute;top:2114px;left:0;width:1200px;height:325px;background:#fff}
.fcol{position:absolute;top:26px}
.fcol h6{font-size:12.5px;font-weight:700;padding-bottom:6px;border-bottom:1px solid #ddd;margin-bottom:12px;white-space:nowrap}
.fcol p,.fcol li{font-size:10.5px;line-height:1.45;color:#444}
.fcol ul{list-style:none}
.fcol li.active{color:var(--green);font-weight:600}
.flogo{display:flex;align-items:center;gap:8px;margin-bottom:12px}
.flogo i{display:block;width:54px;height:54px;background:var(--green)}
.flogo b{font-size:15px;color:var(--green)}
.follow{display:flex;align-items:center;gap:6px;margin-top:22px;font-size:10.5px;font-weight:700}
.follow i{display:block;width:12px;height:12px;border-radius:50%;background:var(--green)}
.fcol p.copy{margin-top:10px;font-size:9.5px;white-space:nowrap}
.badge{width:130px;height:140px;margin:6px 0 0 8px;background:linear-gradient(180deg,#b6dd5c,#6fb53a);border-radius:50%}
.form h6{border:none;font-size:11.5px;line-height:1.4;margin-bottom:12px}
.form h6 span{color:var(--green)}
.fields{display:grid;grid-template-columns:1fr 1fr;gap:8px 16px}
.field{height:30px;background:var(--field);font-size:10px;color:#999;padding:8px 14px}
.field.wide{grid-column:1/3;height:72px}
</style>
</head>
<body>

<header class="site-header">
  <div class="brand"><span class="brand-mark"></span><span class="brand-name">Turf Tidings</span></div>
  <div class="tagline"><h2>LAWN SPECIALISTS</h2><p>from ground preparation to lawn aftercare</p></div>
  <div class="contact">
    <small>SERVICING THE AUCKLAND REGION</small>
    <div class="phone"><svg width="18" height="20" viewBox="0 0 24 24"><path fill="#3aa63c" d="M6.6 10.8a15.1 15.1 0 0 0 6.6 6.6l2.2-2.2c.3-.3.7-.4 1-.2 1.1.4 2.3.6 3.6.6.6 0 1 .4 1 1V20c0 .6-.4 1-1 1A17 17 0 0 1 3 4c0-.6.4-1 1-1h3.5c.6 0 1 .4 1 1 0 1.3.2 2.5.6 3.6.1.3 0 .7-.2 1z"/></svg>0800 24 68 10</div>
  </div>
</header>

<nav class="main-nav">
  <ul>
    <li class="active" style="width:68px">Home</li>
    <li style="width:86px">About us</li>
    <li style="width:86px">Services</li>
    <li style="width:93px">Lawn care</li>
    <li style="width:120px">Seasonal care</li>
    <li style="width:112px">Hydroseeding</li>
    <li style="width:65px">FAQs</li>
    <li style="width:117px">Before &amp; after</li>
    <li style="width:80px">Gallery</li>
    <li style="width:134px;border-right:none">Quote / Contact</li>
  </ul>
</nav>

<section class="wrap hero">
  <div class="hero-photos">
    <div class="photo-before" role="img" aria-label="Bare soil garden area before grass seeding"></div>
    <div class="photo-after" role="img" aria-label="Same garden area with a lush new lawn after grass seeding"></div>
  </div>
  <div class="hero-label" style="left:185px;top:117px">Befor Grass Seeding</div>
  <div class="hero-label" style="left:479px;top:136px">After Grass Seeding</div>
  <div class="hero-arrow" style="left:-2px"><svg width="8" height="12"><path d="M7 1 2 6l5 5" stroke="#fff" stroke-width="2" fill="none"/></svg></div>
  <div class="hero-arrow" style="right:-2px"><svg width="8" height="12"><path d="m1 1 5 5-5 5" stroke="#fff" stroke-width="2" fill="none"/></svg></div>
</section>
<div class="hero-shadow"></div>

<div class="grass" style="top:524px;height:48px" role="img" aria-label="Band of grass blades"></div>

<section class="intro">
  <h1>You can always spot an Turf Tidings lawn</h1>
  <h3>It’s the one that turns your neighbours green with envy.</h3>
  <div class="rule"></div>
  <div class="cols">
    <p>If you want a lawn or playing field that looks good throughout the year, talk to us. Turf Tidings are New Zealand’s experts in high quality grass seeding and lawn maintenance, creating the lushest lawns you’ll ever see. With high-tech equipment, years of experience and expert aftercare, nobody knows grass like Turf Tidings.</p>
    <p>There are many factors that influence the quality of a lawn, including seasonality, growing conditions, shade, seed types, and time. A one-size-fits-all solution couldn’t possibly guarantee a great lawn, so we provide personalised advice, a full range of seeding techniques</p>
  </div>
</section>

<section class="services">
  <article class="card" style="left:119px;top:27px">
    <h4>Grass seeding services</h4>
    <div class="pic" role="img" aria-label="Freshly hydroseeded garden bed" style="background:linear-gradient(180deg,#8f9a7e 0%,#5f8a70 40%,#3f8a86 100%)"></div>
    <p>With a wide range of grass seed applications to choose from, including hydroseeding and instant lawn, there is an option to suit your property and your requirements.</p>
    <span class="btn">More about grass seeding</span>
  </article>
  <article class="card" style="left:611px;top:27px">
    <h4>Lawn care maintenance</h4>
    <div class="pic" role="img" aria-label="Sprinkler watering a green lawn" style="background:linear-gradient(180deg,#7fc24a 0%,#4f9a2a 60%,#3b7f20 100%)"></div>
    <p>As well as lawn care services, the team at Turf Tidings provides helpful information for regular upkeep of your residential or commercial lawn.</p>
    <span class="btn">More about ongoing lawn care</span>
  </article>
  <article class="card" style="left:119px;top:367px">
    <h4>FAQs about grass seeding and lawn care</h4>
    <div class="pic" role="img" aria-label="Raised lawn bed beside a fence and tree" style="background:linear-gradient(180deg,#c9c4b4 0%,#8aa96a 45%,#4fa22c 75%,#d8d8d2 100%)"></div>
    <p>For more information, read our frequently asked questions regarding grass seeding and lawn care.</p>
    <span class="btn">Grass seeding &amp; lawn care FAQs</span>
  </article>
  <article class="card" style="left:611px;top:367px">
    <h4>Before and after lawn photos</h4>
    <div class="pic" role="img" aria-label="Side-by-side view of a lawn area before and after seeding" style="background:linear-gradient(90deg,#9aa3a6 0%,#4f8f86 45%,#5aa232 55%,#6a7378 100%)"></div>
    <p>See what you potential new lawn could look like by viewing a range of before and after lawn seeding photos.</p>
    <span class="btn">Before and after photos</span>
  </article>
</section>

<h3 class="wrap video-title">Watch the video on how Turf Tidings can transform your empty spaces into beautiful green grass lawns</h3>
<div class="video" role="img" aria-label="Video still of a front garden with a new green lawn">
  <div class="play"><span><svg width="18" height="20"><path d="M2 1v18l15-9z" fill="#333"/></svg></span>PLAY VIDEO</div>
</div>
<div class="video-shadow"></div>

<aside class="why">
  <h3>Turf <em>Tidings..</em></h3>
  <ul>
    <li><svg width="14" height="14" viewBox="0 0 14 14"><rect x=".5" y=".5" width="13" height="13" fill="none" stroke="#3aa63c"/><path d="m3 7 3 3 6-7" stroke="#3aa63c" stroke-width="2" fill="none"/></svg>For all things grass, you need the best! Turf Tidings are skilled specialists when it comes to creating the perfect lawn for your property.</li>
    <li><svg width="14" height="14" viewBox="0 0 14 14"><rect x=".5" y=".5" width="13" height="13" fill="none" stroke="#3aa63c"/><path d="m3 7 3 3 6-7" stroke="#3aa63c" stroke-width="2" fill="none"/></svg>From pre-seeding preparation to a full range of grass seeding services and lawn after care options, you’ll enjoy a healthy green lawn for many years.</li>
    <li><svg width="14" height="14" viewBox="0 0 14 14"><rect x=".5" y=".5" width="13" height="13" fill="none" stroke="#3aa63c"/><path d="m3 7 3 3 6-7" stroke="#3aa63c" stroke-width="2" fill="none"/></svg>Selling your property? Turf Tidings will add the wow factor to the outdoor areas of your home with a lush green lawn.</li>
  </ul>
  <span class="btn" style="margin-top:14px">Find out more</span>
</aside>

<section class="testimonial">
  <h5>“I would recommend Turf Tidings to anyone who wants an amazing lawn”</h5>
  <blockquote class="quote"><span class="mark">“</span>Testimonial here about how great Turf Tidings were to deal with and how they are so happy with the lawn and the after care services etc etc.</blockquote>
  <div class="quote-tail"></div>
  <div class="cite"><b>Sam Whitfield</b>Homeowner, Albany</div>
  <div class="pic" role="img" aria-label="Lawn mower on a striped green lawn"></div>
</section>

<footer class="site-footer">
  <div class="fcol" style="left:119px;width:212px">
    <h6>Company Info</h6>
    <div class="flogo"><i></i><b>Turf Tidings</b></div>
    <p>Contrary to popular belief, Lorem Ipsum is not simply random text. It has roots in a piece of classical Latin literature from 45 BC, making it over 2000 years old.</p>
    <div class="follow">Follow us <i></i><i></i><i></i></div>
    <p class="copy">© 2014 Turf Tidings All right reserved Term of Use</p>
  </div>
  <div class="fcol" style="left:352px;width:155px">
    <h6>Navigation</h6>
    <ul>
      <li class="active">Home</li><li>About us</li><li>Services</li><li>Lawn care</li><li>Seasonal care</li><li>Hydroseeding</li><li>FAQs</li><li>Before &amp; After Gallery</li><li>Quote / Contact</li>
    </ul>
  </div>
  <div class="fcol" style="left:529px;width:155px">
    <h6>Diploma In Horticulture</h6>
    <div class="badge" role="img" aria-label="Horticulture diploma badge"></div>
  </div>
  <div class="fcol form" style="left:719px;width:361px">
    <h6>Get a quote for your new lawn!<br>Fill in the form or phone us on <span>0800 24 68 10.</span></h6>
    <div class="fields">
      <div class="field">First Name</div><div class="field">First Name</div>
      <div class="field">First Name</div><div class="field">First Name</div>
      <div class="field wide"></div>
    </div>
    <span class="btn" style="margin-top:12px">Call me back</span>
  </div>
  <div class="grass" style="top:284px;height:41px" role="img" aria-label="Band of grass blades"></div>
</footer>

</body>
</html>
```